Landscaping flier 2024

Create a 1 page flier for landscaping services
1. Must be completed in Adobe Photoshop
2. Size 8.5" x 11" (portrait layout)
3. Include logo
4. Text to include:
2024 Gravesite Landscaping Packages
info@maplecrestmemorial.example
(201) 555-0148
maplecrestmemorial.example
5. Use chart text for the content. DO NOT COPY THE CHART DESIGN/FORMAT. Use the chart for the text you need only.
6. Use "Pricing cards as format for laying out the chart". Open to other ideas as well.
**Use the example of chart design (handwritten) to base your design off of.
7. Photos
-include before and after care photos

```html
<!DOCTYPE html>
<html lang="en">
<head>
<meta charset="utf-8">
<title>2024 Gravesite Landscaping Packages – Maplecrest Memorial</title>
<link rel="stylesheet" href="https://fonts.googleapis.com/css2?family=Anton&family=Red+Hat+Display:wght@400;500;700;900&family=Source+Serif+4:ital,opsz,wght@0,8..60,600;1,8..60,700&display=swap">
<style>
  :root {
    --maroon: #7a0d1f;
    --crimson: #a51d2f;
    --ink: #231f20;
    --paper: #ffffff;
    --paper-soft: #f1f1f1;
    --row-alt: #ececec;
    --rule: #b9b9b9;
    --stage: #a4a4a4;
  }
  * { box-sizing: border-box; margin: 0; padding: 0; }
  html, body { width: 1200px; height: 1117px; overflow: hidden; }
  body { background: var(--stage); font-family: "Red Hat Display", sans-serif; position: relative; }

  .flier {
    position: absolute; left: 184px; top: 20px;
    width: 1256px; height: 1627px;
    transform: scale(0.6624); transform-origin: 0 0;
    background: var(--paper); overflow: hidden;
  }
  .flier-shapes { position: absolute; inset: 0; }

  .brand {
    position: absolute; left: 110px; top: 72px; width: 480px;
    display: flex; align-items: center; justify-content: center; gap: 16px;
    font-family: "Source Serif 4", serif; font-weight: 600;
    font-size: 36px; color: var(--maroon); letter-spacing: 1px;
  }
  .brand-dot { width: 40px; height: 40px; border: 3px solid var(--maroon); border-radius: 50%; }

  .headline-year {
    position: absolute; left: 120px; top: 169px;
    font-family: "Anton", sans-serif; font-size: 241px; line-height: 1;
    color: var(--maroon); letter-spacing: -4px;
  }
  .headline-title {
    position: absolute; left: 112px; top: 399px;
    font-family: "Anton", sans-serif; font-size: 130px; line-height: 1;
    color: var(--ink); letter-spacing: -2px;
  }
  .headline-sub {
    position: absolute; left: 116px; top: 522px;
    font-family: "Source Serif 4", serif; font-style: italic; font-weight: 700;
    font-size: 46px; color: var(--ink);
  }

  .popular-tab {
    position: absolute; left: 884px; top: 568px; width: 260px; height: 50px;
    background: var(--crimson); border-radius: 16px 16px 0 0;
    font-family: "Source Serif 4", serif; font-style: italic; font-weight: 700;
    color: #fff; font-size: 30px; line-height: 48px; text-align: center;
  }

  .packages {
    position: absolute; left: 114px; top: 616px; width: 1030px; height: 724px;
    border: 4px solid var(--maroon); border-radius: 24px; overflow: hidden;
    display: grid;
    grid-template-columns: 251px 260px 255px 1fr;
    grid-template-rows: 120px 111px repeat(6, 60px) 1fr;
    background: var(--paper);
  }
  .cell { display: flex; align-items: center; padding: 0 16px 0 26px; }
  .cell.center { justify-content: center; text-align: center; padding: 0 8px; }
  .col-mid { border-left: 2px solid var(--rule); }
  .col-best { border-left: 6px solid var(--maroon); border-right: 4px solid var(--maroon); }
  .row-alt { background: var(--row-alt); }

  .head { background: var(--ink); color: #fff; flex-direction: column; align-items: flex-start; justify-content: center; padding: 0 10px 0 18px; }
  .head.col-best { background: var(--maroon); padding-left: 16px; }
  .head-label { font-weight: 900; font-size: 40px; line-height: 0.92; padding-left: 12px; }
  .plan-name { font-weight: 900; font-size: 23px; line-height: 1.05; white-space: nowrap; }
  .plan-note { font-weight: 700; font-size: 15px; line-height: 1.08; margin-top: 5px; white-space: nowrap; }

  .service { font-weight: 900; font-size: 16px; line-height: 1.1; color: var(--ink); padding: 0 8px 0 32px; }
  .detail { font-size: 17.5px; line-height: 1.1; color: var(--ink); }
  .detail.col-best { padding: 0 10px 0 16px; }
  .yes { font-weight: 900; font-size: 33px; color: var(--maroon); }
  .no-icon { width: 34px; height: 34px; }

  .price { flex-direction: column; justify-content: center; color: var(--maroon); }
  .price.col-best { background: var(--maroon); color: #fff; }
  .valid-label { font-weight: 500; font-size: 23px; }
  .valid-date { font-weight: 900; font-size: 38px; line-height: 1.05; }
  .terms { display: flex; gap: 8px; }
  .term { display: flex; flex-direction: column; align-items: center; }
  .term-tag { background: var(--maroon); color: #fff; font-size: 14px; padding: 2px 9px; }
  .term-cost { font-weight: 900; font-size: 24px; margin-top: 4px; }
  .fine { font-size: 14px; line-height: 1.1; white-space: nowrap; }
  .big-price { font-weight: 900; font-size: 66px; line-height: 1; margin: 2px 0 4px; }

  .contact { position: absolute; left: 92px; top: 1396px; color: #fff; }
  .contact-row { display: flex; align-items: center; gap: 14px; }
  .phone { font-family: "Anton", sans-serif; font-size: 76px; line-height: 1.1; }
  .line { font-weight: 700; font-size: 28px; margin-top: 8px; padding-left: 4px; }
</style>
</head>
<body>
<div class="flier">
  <svg class="flier-shapes" viewBox="0 0 1256 1627" width="1256" height="1627">
    <defs>
      <linearGradient id="lawn" x1="0" y1="0" x2="0" y2="1">
        <stop offset="0" stop-color="#6e8f48"/>
        <stop offset="0.45" stop-color="#8fb35a"/>
        <stop offset="1" stop-color="#4f7a2c"/>
      </linearGradient>
      <linearGradient id="overgrown" x1="0" y1="0" x2="0" y2="1">
        <stop offset="0" stop-color="#8f9a86"/>
        <stop offset="1" stop-color="#5f8f30"/>
      </linearGradient>
      <linearGradient id="groomed" x1="0" y1="0" x2="0" y2="1">
        <stop offset="0" stop-color="#48663a"/>
        <stop offset="1" stop-color="#6fa23a"/>
      </linearGradient>
    </defs>
    <rect x="0" y="0" width="1256" height="600" fill="var(--paper-soft)"/>
    <rect x="0" y="0" width="32" height="570" fill="var(--maroon)"/>
    <circle cx="1080" cy="308" r="460" fill="var(--maroon)"/>
    <circle cx="1080" cy="308" r="422" fill="var(--paper)"/>
    <circle cx="1080" cy="308" r="408" fill="url(#lawn)" role="img" aria-label="Photo of a well-kept cemetery lawn with headstones and trees"/>
    <rect x="32" y="1204" width="596" height="423" fill="var(--maroon)"/>
    <rect x="628" y="1204" width="628" height="423" fill="url(#lawn)" role="img" aria-label="Photo of cemetery grounds"/>
    <rect x="628" y="1363" width="311" height="264" fill="url(#overgrown)" role="img" aria-label="Before photo: overgrown grave plot"/>
    <rect x="939" y="1363" width="6" height="264" fill="var(--paper)"/>
    <rect x="945" y="1363" width="311" height="264" fill="url(#groomed)" role="img" aria-label="After photo: trimmed boxwood bed on grave"/>
    <rect x="92" y="600" width="1072" height="763" rx="40" fill="var(--paper)"/>
  </svg>

  <div class="brand"><span>MAPLECREST</span><span class="brand-dot"></span><span>MEMORIAL</span></div>

  <div class="headline-year">2024</div>
  <div class="headline-title">Gravesite</div>
  <div class="headline-sub">Landscaping Packages</div>

  <div class="popular-tab">Most Popular</div>

  <div class="packages">
    <div class="cell head"><div class="head-label">SERVICES<br>OFFERED</div></div>
    <div class="cell head col-mid"><div class="plan-name">SEASONAL<br>CARE</div><div class="plan-note">Seasonal Landscaping<br>grave care.</div></div>
    <div class="cell head col-mid"><div class="plan-name">BASIC CARE<br>ENDOWMENT</div><div class="plan-note">Landscdaping care forever<br>for graves with no plantings.</div></div>
    <div class="cell head col-best"><div class="plan-name">PERPETUAL CARE<br>ENDOWMENT</div><div class="plan-note">landscaping care forever<br>for graves with piantings.</div></div>

    <div class="cell row-alt service">WEEDING &amp; TRIMMING<br>ON YOUR GRAVESITE</div>
    <div class="cell row-alt col-mid detail">Approximately every 7 weeks during the growing season: mid-April through mid-October</div>
    <div class="cell row-alt col-mid detail" style="padding-left:62px">2 times per yaer:<br>mid-May &amp;<br>mid-September</div>
    <div class="cell row-alt col-best detail">Approximately every 7 weeks during the growing season: mid-April through mid-October</div>

    <div class="cell service">PAYMENT ENSURES<br>GRAVE CARE FOREVER</div>
    <div class="cell center col-mid"><svg class="no-icon" viewBox="0 0 34 34"><circle cx="17" cy="17" r="14" fill="none" stroke="var(--maroon)" stroke-width="4"/><line x1="8" y1="26" x2="26" y2="8" stroke="var(--maroon)" stroke-width="4"/></svg></div>
    <div class="cell center col-mid yes">YES</div>
    <div class="cell center col-best yes">YES</div>

    <div class="cell row-alt service">MONUMENT LEVELING</div>
    <div class="cell row-alt center col-mid"><svg class="no-icon" viewBox="0 0 34 34"><circle cx="17" cy="17" r="14" fill="none" stroke="var(--maroon)" stroke-width="4"/><line x1="8" y1="26" x2="26" y2="8" stroke="var(--maroon)" stroke-width="4"/></svg></div>
    <div class="cell row-alt center col-mid yes">YES</div>
    <div class="cell row-alt center col-best yes">YES</div>

    <div class="cell service">MONUMENT CLEANING</div>
    <div class="cell center col-mid"><svg class="no-icon" viewBox="0 0 34 34"><circle cx="17" cy="17" r="14" fill="none" stroke="var(--maroon)" stroke-width="4"/><line x1="8" y1="26" x2="26" y2="8" stroke="var(--maroon)" stroke-width="4"/></svg></div>
    <div class="cell center col-mid"><svg class="no-icon" viewBox="0 0 34 34"><circle cx="17" cy="17" r="14" fill="none" stroke="var(--maroon)" stroke-width="4"/><line x1="8" y1="26" x2="26" y2="8" stroke="var(--maroon)" stroke-width="4"/></svg></div>
    <div class="cell center col-best yes">YES</div>

    <div class="cell row-alt service">FULL BED OF<br>BOXWOOD SHRUBS</div>
    <div class="cell row-alt center col-mid"><svg class="no-icon" viewBox="0 0 34 34"><circle cx="17" cy="17" r="14" fill="none" stroke="var(--maroon)" stroke-width="4"/><line x1="8" y1="26" x2="26" y2="8" stroke="var(--maroon)" stroke-width="4"/></svg></div>
    <div class="cell row-alt center col-mid"><svg class="no-icon" viewBox="0 0 34 34"><circle cx="17" cy="17" r="14" fill="none" stroke="var(--maroon)" stroke-width="4"/><line x1="8" y1="26" x2="26" y2="8" stroke="var(--maroon)" stroke-width="4"/></svg></div>
    <div class="cell row-alt center col-best yes">YES</div>

    <div class="cell service">REPLACEMENT<br>OF SHRUBS</div>
    <div class="cell center col-mid"><svg class="no-icon" viewBox="0 0 34 34"><circle cx="17" cy="17" r="14" fill="none" stroke="var(--maroon)" stroke-width="4"/><line x1="8" y1="26" x2="26" y2="8" stroke="var(--maroon)" stroke-width="4"/></svg></div>
    <div class="cell center col-mid"><svg class="no-icon" viewBox="0 0 34 34"><circle cx="17" cy="17" r="14" fill="none" stroke="var(--maroon)" stroke-width="4"/><line x1="8" y1="26" x2="26" y2="8" stroke="var(--maroon)" stroke-width="4"/></svg></div>
    <div class="cell center col-best yes">YES</div>

    <div class="cell row-alt service">TRUST CERTIFICATE</div>
    <div class="cell row-alt center col-mid"><svg class="no-icon" viewBox="0 0 34 34"><circle cx="17" cy="17" r="14" fill="none" stroke="var(--maroon)" stroke-width="4"/><line x1="8" y1="26" x2="26" y2="8" stroke="var(--maroon)" stroke-width="4"/></svg></div>
    <div class="cell row-alt center col-mid"><svg class="no-icon" viewBox="0 0 34 34"><circle cx="17" cy="17" r="14" fill="none" stroke="var(--maroon)" stroke-width="4"/><line x1="8" y1="26" x2="26" y2="8" stroke="var(--maroon)" stroke-width="4"/></svg></div>
    <div class="cell row-alt center col-best yes">YES</div>

    <div class="cell center price"><div class="valid-label">Valid through</div><div class="valid-date">10/31/2022</div></div>
    <div class="cell center price col-mid">
      <div class="terms">
        <div class="term"><span class="term-tag">3 Years</span><span class="term-cost">$396</span></div>
        <div class="term"><span class="term-tag">3 Years</span><span class="term-cost">$264</span></div>
        <div class="term"><span class="term-tag">3 Years</span><span class="term-cost">$132</span></div>
      </div>
      <div class="fine" style="margin-top:6px">Multi-year payment locks in<br>current rates.</div>
    </div>
    <div class="cell center price col-mid"><div class="fine">12 monthly payments of</div><div class="big-price">$287</div><div class="fine">Call for single payment discount.</div></div>
    <div class="cell center price col-best"><div class="fine">12 monthly payments of</div><div class="big-price">$351</div><div class="fine">Call for single payment discount.</div></div>
  </div>

  <div class="contact">
    <div class="contact-row">
      <svg width="64" height="64" viewBox="0 0 64 64" aria-hidden="true"><circle cx="32" cy="32" r="28" fill="none" stroke="#fff" stroke-width="5"/><path d="M22 18c3-2 5 0 7 4 2 3 1 5-1 6 1 4 5 8 9 9 1-2 3-3 6-1 4 2 6 4 4 7-2 3-6 5-11 2-7-4-13-10-16-17-2-5 0-8 2-10z" fill="#fff"/></svg>
      <span class="phone">(201) 555-0148</span>
    </div>
    <div class="contact-row line">
      <svg width="36" height="28" viewBox="0 0 36 28" aria-hidden="true"><rect x="2" y="2" width="32" height="24" fill="none" stroke="#fff" stroke-width="3"/><path d="M2 2l16 13L34 2" fill="none" stroke="#fff" stroke-width="3"/></svg>
      <span>info@maplecrestmemorial.example</span>
    </div>
    <div class="contact-row line">
      <svg width="36" height="36" viewBox="0 0 36 36" aria-hidden="true"><circle cx="18" cy="18" r="15" fill="none" stroke="#fff" stroke-width="3"/><ellipse cx="18" cy="18" rx="7" ry="15" fill="none" stroke="#fff" stroke-width="2.5"/><path d="M3 18h30M6 10h24M6 26h24" stroke="#fff" stroke-width="2.5"/></svg>
      <span>maplecrestmemorial.example</span>
    </div>
  </div>
</div>
</body>
</html>
```